Real Estate Website Design Needed of IDX Intergration

I need a 'Lead Capture' Website the will be use for marketing to site visitors looking to buy a home/land in Central Florida (Greater Orlando, Florida), United States.

Competitor Websites that I like;

Bramwellcrew.com (Like the Most)
TheKolvaxCircle.com (Good One-Line Property Search Form)
TheMarbos.com (Good 'High-End' Look)
FreshCozyPathKessler.com (Good Property Search Form)
Updates

The project title should be; "Real Estate Website Design Needed FOR IDX Intergration"

Target Market(s)

Consumers looking to purchase homes or land in the Central Florida, United States

Industry/Entity Type

Real Estate

Logo Text

Go Trade Nest Harbor or GoTradeNestHarbor or Go TradeNest Harbor

Number of Pages Required

1 page

Font styles to use
Serif
Sans Serif

Colors

Designer to choose colors to be used in the design.

Requirements
Must have
• Our Team Name: 'GoTradeNestHarbor Real Estate Team' is an important part of the design. Our Contact information needs to be apart of the design; Phone Number: (555) 814-3926 Email: ContactUs@GoTradeNestHarbor.example MOST IMPORTANTLY we must have Opt-In Buttons/Contact Form 'above the break' of the site, see a great example at Bramwellcrew.com
• Other Needs;
• -Search Engine Friendly Design
• -The attached must be present in the footnote of the design

```html
<!DOCTYPE html>
<html lang="en">
<head>
<meta charset="utf-8">
<title>Go Trade Nest Harbor – Central Florida Real Estate</title>
<link rel="stylesheet" href="https://fonts.googleapis.com/css2?family=Montserrat:wght@600;700;800&family=Open+Sans:ital,wght@0,400;0,600;0,700;1,400&display=swap">
<style>
:root{
  --blue:#0f5490;
  --blue-dark:#0b4475;
  --ink:#222;
  --text:#444;
  --muted:#666;
  --line:#bcbcbc;
  --grey-bg:#efefef;
  --white:#fff;
  --head:"Montserrat",sans-serif;
  --body:"Open Sans",sans-serif;
}
*{box-sizing:border-box;margin:0;padding:0}
html,body{width:1200px;height:2922px;overflow:hidden}
body{font-family:var(--body);color:var(--text);background:var(--white);position:relative}
.abs{position:absolute}

/* header */
.site-header{position:absolute;top:0;left:0;width:1200px;height:115px;background:var(--white)}
.brand{position:absolute;left:100px;top:36px;display:flex;align-items:center;gap:12px}
.brand-mark{width:34px;height:34px;border:3px solid var(--blue)}
.brand-name{font-family:var(--head);font-weight:800;font-size:22px;color:var(--blue);letter-spacing:.3px;line-height:1}
.main-nav{position:absolute;top:48px;right:98px;display:flex;gap:40px}
.main-nav a{font-family:var(--body);font-weight:600;font-size:15px;color:var(--ink);text-decoration:none;letter-spacing:.2px}

/* hero */
.hero{position:absolute;top:115px;left:0;width:1200px;height:515px;
  background:linear-gradient(180deg,#3b3f66 0%,#5a4a72 28%,#2a2c45 55%,#1c1b2c 75%,#34253a 100%)}
.hero-title{position:absolute;left:100px;top:125px;font-family:var(--head);font-weight:800;font-size:42px;color:var(--white);letter-spacing:.5px}
.hero-lede{position:absolute;left:100px;top:205px;width:420px;font-size:15px;line-height:34px;color:var(--white);font-weight:600}
.btn{display:inline-flex;align-items:center;justify-content:center;font-family:var(--body);font-weight:600;font-size:14px;letter-spacing:.3px;text-decoration:none;border-radius:3px}
.hero .btn-light{position:absolute;left:100px;top:317px;width:237px;height:52px;background:var(--white);color:var(--ink)}
.hero .btn-ghost{position:absolute;left:365px;top:317px;width:263px;height:52px;border:2px solid var(--white);color:var(--white)}
.hero-arrow{position:absolute;top:235px}

/* search panel */
.search-panel{position:absolute;left:722px;top:65px;width:378px;height:387px;background:var(--white);box-shadow:0 2px 8px rgba(0,0,0,.25)}
.search-panel h2{height:52px;background:var(--blue);color:var(--white);font-family:var(--head);font-weight:700;font-size:21px;text-align:center;line-height:52px;letter-spacing:.3px}
.field{position:absolute;left:20px;width:338px;height:40px;border:1px solid var(--line);font-size:12px;color:#777;padding:0 14px;display:flex;align-items:center;gap:6px}
.lbl{position:absolute;font-size:12px;font-weight:600;color:var(--ink)}
.select{position:absolute;width:160px;height:40px;border:1px solid var(--line);font-size:12px;color:#777;display:flex;align-items:center;padding-left:12px}
.select::after{content:"";position:absolute;right:0;top:0;width:36px;height:38px;border-left:1px solid var(--line)}
.select svg{position:absolute;right:13px;top:16px}
.search-btn{position:absolute;left:20px;top:320px;width:108px;height:46px;background:var(--blue);color:var(--white)}
.adv-link{position:absolute;left:146px;top:336px;font-size:12px;color:var(--muted);text-decoration:underline;font-weight:600;letter-spacing:.3px}

/* about */
.kicker{position:absolute;left:0;width:1200px;text-align:center;font-size:21px;color:var(--ink);letter-spacing:.5px}
.section-title{position:absolute;left:0;width:1200px;text-align:center;font-family:var(--head);font-weight:800;color:var(--blue)}
.about-title{top:732px;font-size:34px;line-height:46px}
.about-copy{position:absolute;left:118px;top:850px;width:964px;text-align:center;font-size:13.5px;line-height:26px;color:var(--text)}
.btn-solid{background:var(--blue);color:var(--white)}
.btn-outline{border:1.5px solid #444;color:var(--ink);background:var(--white)}

/* featured */
.featured{position:absolute;top:1105px;left:0;width:1200px;height:652px;background:var(--grey-bg)}
.rule{position:absolute;left:560px;width:80px;height:3px;background:var(--blue)}
.listing{position:absolute;top:157px;width:315px;height:418px;background:var(--white);box-shadow:0 1px 6px rgba(0,0,0,.15);border-radius:3px}
.listing-photo{position:absolute;left:7px;top:8px;width:301px;height:184px;border-radius:3px}
.price{position:absolute;left:7px;top:149px;width:118px;height:43px;background:rgba(40,40,40,.88);color:var(--white);font-weight:700;font-size:18px;display:flex;align-items:center;padding-left:14px;border-bottom-left-radius:3px}
.addr{position:absolute;left:8px;top:212px;font-size:13px;font-weight:600;color:var(--ink)}
.city{position:absolute;left:8px;top:231px;font-family:var(--head);font-weight:700;font-size:17px;color:var(--ink)}
.city.active{color:var(--blue)}
.listing p{position:absolute;left:8px;top:265px;width:295px;font-size:13px;line-height:22px;color:var(--text)}
.listing .btn{position:absolute;left:8px;top:347px;width:114px;height:46px;font-size:13px}

/* testimonials */
.quote-mark{position:absolute;left:555px;top:1928px}
.testimonial{position:absolute;left:135px;top:2007px;width:930px;text-align:center;font-style:italic;font-size:14px;line-height:27px;color:var(--text)}
.author{position:absolute;left:0;top:2118px;width:1200px;text-align:center;font-weight:700;font-size:15px;color:var(--blue)}

/* footer */
.site-footer{position:absolute;top:2315px;left:0;width:1200px;height:607px;background:var(--grey-bg);border-top:4px solid var(--blue-dark)}
.footer-brand{position:absolute;top:65px;left:0;width:1200px;display:flex;justify-content:center;align-items:center;gap:12px}
.badge{position:absolute;top:168px;width:168px;height:75px;border:2px solid var(--blue);background:var(--white);border-radius:3px}
.badge span{position:absolute;left:50%;top:50%;transform:translate(-50%,-50%);background:#d6d6d6}
.footer-nav{position:absolute;top:282px;left:0;width:1200px;display:flex;justify-content:center;gap:30px;font-weight:600;font-size:15px;color:var(--ink)}
.footer-nav a{color:var(--ink);text-decoration:none}
.legal{position:absolute;left:100px;width:1000px;text-align:center;font-size:13px;line-height:22px;color:var(--ink)}
.footer-rule{position:absolute;left:100px;top:2853px;width:1000px;height:1px;background:#999}
.copyright{position:absolute;left:0;top:2878px;width:1200px;text-align:center;font-size:13px;font-weight:600;color:var(--ink)}
</style>
</head>
<body>

<header class="site-header">
  <div class="brand"><span class="brand-mark"></span><span class="brand-name">GO TRADE NEST HARBOR</span></div>
  <nav class="main-nav">
    <a href="#">HOME</a><a href="#">WHO WE ARE</a><a href="#">SEARCH HOMES FOR SALE</a><a href="#">BLOG</a><a href="#">CONTACT</a>
  </nav>
</header>

<section class="hero" role="img" aria-label="Night skyline of downtown Orlando reflected in a lake">
  <svg class="hero-arrow" style="left:34px" width="24" height="46" viewBox="0 0 24 46"><path d="M22 2 2 23l20 21" fill="none" stroke="#fff" stroke-width="2.5"/></svg>
  <svg class="hero-arrow" style="right:34px" width="24" height="46" viewBox="0 0 24 46"><path d="M2 2l20 21L2 44" fill="none" stroke="#fff" stroke-width="2.5"/></svg>
  <h1 class="hero-title">GO TRADE NEST HARBOR</h1>
  <p class="hero-lede">Nemo enim ipsam voluptatem quia voluptas sit aspernatur aut odit aut fugit, sed quia consequuntur.</p>
  <a class="btn btn-light" href="#">SEARCH HOMES FOR SALE</a>
  <a class="btn btn-ghost" href="#">WHAT'S YOUR HOME WORTH</a>

  <form class="search-panel">
    <h2>SEARCH LISTINGS</h2>
    <div class="field" style="top:70px">Property Type</div>
    <div class="field" style="top:122px">
      <svg width="9" height="12" viewBox="0 0 9 12"><path d="M4.5 0A4.5 4.5 0 0 0 0 4.5C0 8 4.5 12 4.5 12S9 8 9 4.5A4.5 4.5 0 0 0 4.5 0zm0 6.3a1.8 1.8 0 1 1 0-3.6 1.8 1.8 0 0 1 0 3.6z" fill="#444"/></svg>
      Enter Country, City or Zipcode</div>
    <span class="lbl" style="left:20px;top:172px">PRICE</span>
    <div class="select" style="left:20px;top:193px">From<svg width="10" height="6"><path d="M0 0h10L5 6z" fill="#444"/></svg></div>
    <div class="select" style="left:198px;top:193px">To<svg width="10" height="6"><path d="M0 0h10L5 6z" fill="#444"/></svg></div>
    <span class="lbl" style="left:20px;top:245px">BEDS</span>
    <span class="lbl" style="left:198px;top:245px">BATHS</span>
    <div class="select" style="left:20px;top:266px">Any<svg width="10" height="6"><path d="M0 0h10L5 6z" fill="#444"/></svg></div>
    <div class="select" style="left:198px;top:266px">Any<svg width="10" height="6"><path d="M0 0h10L5 6z" fill="#444"/></svg></div>
    <a class="btn search-btn" href="#">SEARCH</a>
    <a class="adv-link" href="#">ADVANCED SEARCH</a>
  </form>
</section>

<section class="about">
  <p class="kicker" style="top:690px">ABOUT US</p>
  <h2 class="section-title about-title">TRUSTED CENTRAL FLORIDA REAL<br>ESTATE EXPERTS</h2>
  <p class="about-copy">Nemo enim ipsam voluptatem quia voluptas sit aspernatur aut odit aut fugit, sed quia consequuntur magni dolores eos qui ratione voluptatem sequi nesciunt. Neque porro quisquam est, qui dolorem ipsum quia dolor sit amet, consectetur, adipisci velit, sed quia non numquam eius modi tempora incidunt ut labore et dolore magnam aliquam quaerat voluptatem. Ut enim ad minima veniam, quis nostrum exercitationem</p>
  <a class="btn btn-solid abs" style="left:442px;top:978px;width:145px;height:52px" href="#">READ MORE</a>
  <a class="btn btn-outline abs" style="left:606px;top:978px;width:152px;height:52px" href="#">CONTACT US</a>
</section>

<section class="featured">
  <h2 class="section-title" style="top:50px;font-size:26px">FEATURED LISTINGS</h2>
  <span class="rule" style="top:104px"></span>

  <article class="listing" style="left:100px">
    <div class="listing-photo" role="img" aria-label="Modern home with pool lit at dusk" style="background:linear-gradient(160deg,#1d3f7a 0%,#2f5fa8 40%,#c9a56a 70%,#173566 100%)"></div>
    <span class="price">$ 50,000</span>
    <span class="addr">123 REGENT WAY</span>
    <h3 class="city active">Kissimmee, Florida</h3>
    <p>Sed ut perspiciatis unde omnis iste natus error sit voluptatem accusantium doloremque laudan tium.</p>
    <a class="btn btn-solid" href="#">READ MORE</a>
  </article>

  <article class="listing" style="left:442px">
    <div class="listing-photo" role="img" aria-label="Two-storey family house with green lawn" style="background:linear-gradient(180deg,#8fc0ea 0%,#cfe2f0 35%,#8a97a3 55%,#5f9a3c 75%,#4f8a2e 100%)"></div>
    <span class="price">$ 50,000</span>
    <span class="addr">123 REGENT WAY</span>
    <h3 class="city">Winter Springs, Florida</h3>
    <p>Sed ut perspiciatis unde omnis iste natus error sit voluptatem accusantium doloremque laudan tium.</p>
    <a class="btn btn-outline" href="#">READ MORE</a>
  </article>

  <article class="listing" style="left:785px">
    <div class="listing-photo" role="img" aria-label="Suburban house with driveway and garden" style="background:linear-gradient(180deg,#7fb3e4 0%,#b8d3ea 30%,#6f7480 55%,#4c7f35 78%,#9a9a96 100%)"></div>
    <span class="price">$ 50,000</span>
    <span class="addr">123 REGENT WAY</span>
    <h3 class="city">Orlando, Florida</h3>
    <p>Sed ut perspiciatis unde omnis iste natus error sit voluptatem accusantium doloremque laudan tium.</p>
    <a class="btn btn-outline" href="#">READ MORE</a>
  </article>
</section>

<section class="testimonials">
  <h2 class="section-title" style="top:1824px;font-size:26px">OUR TESTIMONIALS</h2>
  <span class="rule" style="top:1878px"></span>
  <svg class="quote-mark" width="90" height="44" viewBox="0 0 90 44">
    <path d="M4 26c0-12 6-20 16-24l2 4c-6 3-9 8-9 13h8v17H4zm22 0c0-12 6-20 16-24l2 4c-6 3-9 8-9 13h8v17H26z" fill="#0f5490"/>
    <path d="M86 18c0 12-6 20-16 24l-2-4c6-3 9-8 9-13h-8V8h17zm-22 0c0 12-6 20-16 24l-2-4c6-3 9-8 9-13h-8V8h17z" fill="#0f5490"/>
  </svg>
  <p class="testimonial">Nemo enim ipsam voluptatem quia voluptas sit aspernatur aut odit aut fugit, sed quia consequuntur magni dolores eos qui ratione vo luptatem sequi nesciunt. Neque porro quisquam est, qui dolorem ipsum quia dolor sit amet, consectetur, adipisci velit, sed quia non numquam eius modi tempora...</p>
  <p class="author">- JOHN SMITH</p>
  <a class="btn btn-solid abs" style="left:528px;top:2183px;width:144px;height:53px" href="#">MORE REVIEWS</a>
</section>

<footer class="site-footer">
  <div class="footer-brand"><span class="brand-mark"></span><span class="brand-name">GO TRADE NEST HARBOR</span></div>
  <div class="badge" style="left:307px" role="img" aria-label="Partner brokerage badge"><span style="width:110px;height:30px"></span></div>
  <div class="badge" style="left:516px" role="img" aria-label="Professional membership badge"><span style="width:34px;height:40px"></span></div>
  <div class="badge" style="left:727px" role="img" aria-label="Equal housing opportunity badge"><span style="width:38px;height:40px"></span></div>
  <nav class="footer-nav">
    <a href="#">HOME</a><span>|</span><a href="#">WHO WE ARE</a><span>|</span><a href="#">SEARCH HOMES FOR SALE</a><span>|</span><a href="#">BLOG</a><span>|</span><a href="#">CONTACT</a>
  </nav>
  <p class="legal" style="top:337px">IDX information is provided exclusively for consumers' personal, noncommercial use, that it may not be used for any purpose other than to identify prospec tive properties consumers maybe interested in purchasing, and that the data is deemed reliable but is not guaranteed accurate by the MLS.</p>
  <p class="legal" style="top:393px">Listing information courtesy of Sunridge Regional MLS. All listing information is deemed reliable but not guaranteed and should be independently verified through personal inspection by appropriate professionals. Listings displayed on this website may be subject to prior sale or removal from sale; availability of any listing should always be independently verified. Listing information is provided for consumer personal, non-commercial use, solely to identify potential properties for potential purchase; all other use is strictly prohibited and may violate relevant federal and state law. Copyright© 2017 Sunridge Regional MLS. All rights reserved.</p>
</footer>
<div class="footer-rule"></div>
<p class="copyright">Copyright © 2017 Go Trade Nest Harbor. All Right Reserved</p>

</body>
</html>
```